4.25" x 11" Door Hanger Design - Glass Bolt Internet Service

We are sourcing a door hanger that will be used to micro target specific neighborhoods with our new "Glass Bolt" internet service offering

This will be used as a template for a new type of plan we are offering in very specific areas. The first will be "Cedar Hollow" with 3 plan offerings.

Stock photos should be family friendly but we want something modern and exciting that we can use to advertise a new internet service offering.
Updates

Sorry if I missed this before, but we would of course like our website and phone number with an encouragement to call us Website: www.brivanet.example Phone: 555-304-2968

Target Market(s)

Residential Internet Service

Industry/Entity Type

Internet Service Provider

Font styles to use
Sans Serif
Other font styles liked:
• RockoFLF

Colors

Designer to choose colors to be used in the design.

Requirements
Must have
• 1) Our logo with "Internet Services" nearby to show "Brivanet Internet Services" (name and what we do)
• 2) "Glass Bolt Internet Service is Now Available in Cedar Hollow!"
• 3) Show three plans, we don't know the price yet and we will edit the winning design eventually when we know the exact price.
• 100 Mbps $XX.XX per month
• 250 Mbps $XX.XX per month
• 1 Gbps $XX.XX per month
• 4) The plan names and prices should be easy to edit in the future if/when we try these in different markets.
• This ad will be modified with specific information like prices and the location when we use it in specific spots.
• We will be using Printwagon for the printing, please use their website for the punch hole location, dimensions, etc.
• https://www.printwagon.example/door-hanger-printing/
Nice to have
• We want to demonstrate far higher than normal internet service speed offerings. This can use whatever you think demonstrates this idea to the customers better, something like a speed test looking logo
Should not have
• Do not copy our website, we want a fresh design

```html
<!DOCTYPE html>
<html lang="en">
<head>
<meta charset="utf-8">
<title>Brivanet Door Hanger – Glass Bolt</title>
<link href="https://fonts.googleapis.com/css2?family=Open+Sans:wght@400;600;700&family=Rubik:wght@500&display=swap" rel="stylesheet">
<style>
  :root {
    --stage: #444444;
    --sky: #6fa3d8;
    --paper: #ffffff;
    --brand-blue: #2a8acb;
    --brand-red: #b81f24;
    --sweater: #b3262d;
    --photo-light: #eef3fa;
  }
  * { margin: 0; padding: 0; box-sizing: border-box; }
  html, body {
    width: 1200px; height: 900px; overflow: hidden;
    background: var(--stage);
    font-family: "Open Sans", sans-serif;
  }
  .door-hanger {
    position: absolute; left: 433px; top: 11px;
    width: 334px; height: 862px;
    background: linear-gradient(to bottom, var(--sky) 0, #c9dcf0 110px, var(--paper) 170px, var(--paper) 500px, #e4ecf7 775px);
    overflow: hidden;
  }
  .hanger-hole {
    position: absolute; left: 115px; top: 31px;
    width: 104px; height: 104px; border-radius: 50%;
    background: var(--stage);
  }
  .brand-mark {
    position: absolute; top: 182px; left: 0; width: 100%;
    display: flex; justify-content: center; align-items: center; gap: 6px;
    color: var(--brand-blue); font-size: 27px; font-weight: 400;
  }
  .brand-mark .dot {
    width: 14px; height: 14px; border-radius: 50%; background: var(--brand-blue);
  }
  .headline { position: absolute; top: 241px; left: 0; width: 100%; text-align: center; }
  .headline .company {
    display: block; color: var(--brand-blue); font-size: 22px; font-weight: 400;
    letter-spacing: 6px; line-height: 26px;
  }
  .headline .service {
    display: block; color: var(--brand-red);
    font-family: "Rubik", sans-serif; font-weight: 500;
    font-size: 47px; line-height: 44px; letter-spacing: -1px;
  }
  .announcement { position: absolute; top: 378px; left: 0; width: 100%; text-align: center; }
  .announcement .lead { color: var(--brand-blue); font-size: 14px; line-height: 20px; }
  .announcement .location {
    color: var(--brand-red); font-size: 21px; font-weight: 700; margin-top: 6px; display: block;
  }
  .hero-photo {
    position: absolute; left: 5px; top: 455px; width: 172px; height: 320px;
    background: linear-gradient(to bottom, var(--photo-light) 0, #d9c5b8 20%, var(--sweater) 35%, #8f1d22 92%, #2d2d33 100%);
    border-radius: 70px 70px 0 0;
  }
  .plan-list {
    position: absolute; left: 190px; top: 470px; width: 130px;
    list-style: none; text-align: center;
  }
  .plan { margin-bottom: 14px; }
  .plan .speed { display: block; color: var(--brand-red); font-weight: 700; font-size: 45px; line-height: 46px; }
  .plan .unit { display: block; color: var(--brand-red); font-weight: 700; font-size: 26px; line-height: 30px; }
  .plan .price { display: block; color: var(--brand-blue); font-weight: 700; font-size: 19px; line-height: 30px; }
  .plan.gig { margin-top: 22px; }
  .plan.gig .unit { font-size: 26px; }
  .phone-band {
    position: absolute; left: 0; top: 775px; width: 100%; height: 52px;
    background: var(--brand-red); color: var(--paper);
    font-size: 36px; font-weight: 700; text-align: center; line-height: 52px;
  }
  .web-band {
    position: absolute; left: 0; top: 827px; width: 100%; height: 35px;
    background: var(--brand-blue); color: var(--paper);
    font-size: 18px; font-weight: 600; text-align: center; line-height: 35px;
    letter-spacing: 0.5px;
  }
</style>
</head>
<body>
  <main class="door-hanger">
    <div class="hanger-hole"></div>

    <div class="brand-mark"><span class="dot"></span><span>Brivanet</span></div>

    <h1 class="headline">
      <span class="company">BRIVANET</span>
      <span class="service">INTERNET</span>
      <span class="service">SERVICES</span>
    </h1>

    <p class="announcement">
      <span class="lead">GLASS BOLT INTERNET SERVICE IS<br>NOW AVAILABLE IN</span>
      <span class="location">CEDAR HOLLOW!</span>
    </p>

    <div class="hero-photo" role="img" aria-label="Smiling man in a red sweater giving a thumbs up"></div>

    <ul class="plan-list">
      <li class="plan"><span class="speed">100</span><span class="unit">MBPS</span><span class="price">$XX.XX Pm</span></li>
      <li class="plan"><span class="speed">250</span><span class="unit">MBPS</span><span class="price">$XX.XX Pm</span></li>
      <li class="plan gig"><span class="unit">1 GBPS</span><span class="price">$XX.XX Pm</span></li>
    </ul>

    <div class="phone-band">555-304-2968</div>
    <div class="web-band">www.brivanet.example</div>
  </main>
</body>
</html>
```